Book Cover Design - Rooted Together: 7 Paths to Raise a Household that Blooms

International cover needed for the Australian (Fenwick Marlow/QRT Press 2011) non-fiction book Rooted Together: 7 Paths to Raise a Household that Blooms.

Blurb: With the birth of a baby, come other new beginnings, the birth of a mother, of a father, and of a family. With each stage of a child's growth, and with every new baby, there are more new beginnings. In older cultures and in villages around the world, parenthood was considered a rite of passage but traditions that guided parents into becoming a family have largely been lost - until now.

This ground breaking book walks a new generation of mothers and fathers through the eight steps of the modern parenthood rite of passage, from couple-connection to family-foundations, so they can prepare for and continue to grow a family that thrives.

Bio: Nora Pembridge is a relationship counsellor, parent educator and columnist for Homeward Nursery magazine. She lives in Sydney with her husband, their three gorgeous children and an itinerary of pets. This is her first book.
Updates

Thank you for your patience, I haven't ever done anything like this before and the designs submitted have helped me to be more specific in my requests. Please see the updated brief. The most important point is that I am seeking a TEXT based cover, so BOTH the TITLE and SUBTITLE should take up most of the space, the image could either be in the background with the title and subtitle overlayed, or be much smaller to fit around them. I have attached some more images to the brief, hope they help to convey the 'feel' I am after.  Thanks again!

Reason: Thank you so much for taking an interest in this project, the process has been very educational and helpful for me. While some of the stock art in the submitted designs are great, I've decided to commission a custom illustration which completely captures the meaning of Rooted Together. I will upload the illustration once it's complete for designers who are still interested to use. Thank you for your patience! Nora

Thank you all for your patience and for opening up my thinking about what I am really hoping for with this cover. I have uploaded some new tree designs and more specific instructions that I would like to be included in the cover design. I'm looking forward to seeing your creations!

With warm regards,

Nora

Target Market(s)

Couples thinking about having a baby and new parents of one or more young children.

Industry/Entity Type

Baby

Requirements
Must have
• TEXT based cover with BOTH the TITLE and SUBTITLE taking up most of the page.
Colors to match the Australian version (see attached)
Tree design bottom left (as per Trunk Treatment image attached) OR Heart Tree Design
Root design (as per one of the two images attached)
PLEASE ADD: three new shoots coming up from the ground under the tree to symbolize the children.
Nice to have
• Artistic effect to complement Australian cover.
Subtle retro feel to complement Australian cover.
Should not have
• The book is inclusive of all parents (including same-sex parents) so no images of mother/father and baby.

```html
<!DOCTYPE html>
<html lang="en">
<head>
<meta charset="utf-8">
<title>Rooted Together – Book Cover</title>
<link rel="stylesheet" href="https://fonts.googleapis.com/css2?family=Oswald:wght@400;500;700&family=Open+Sans:wght@700&display=swap">
<style>
  :root {
    --backdrop: #e9e7ec;
    --cover-paper: #fbfbfb;
    --ink: #111111;
    --label-text: #ffffff;
    --leaf-green: #7cbf3a;
    --leaf-yellow: #e9c92e;
    --leaf-orange: #f09a2c;
    --leaf-purple: #9a6fb6;
    --leaf-blue: #3f9fd6;
    --leaf-pink: #e0508f;
    --trunk-brown: #7a4a2c;
  }
  * { box-sizing: border-box; margin: 0; padding: 0; }
  html, body {
    width: 1200px;
    height: 900px;
    overflow: hidden;
    background: var(--backdrop);
  }
  .stage {
    width: 1200px;
    height: 900px;
    display: flex;
    align-items: center;
    justify-content: center;
  }
  .book-cover {
    position: relative;
    width: 560px;
    height: 840px;
    background: var(--cover-paper);
    overflow: hidden;
    box-shadow: 0 6px 24px rgba(0, 0, 0, 0.12);
  }
  .author-label {
    position: absolute;
    top: 66px;
    left: 0;
    width: 262px;
    height: 50px;
    background: var(--ink);
    color: var(--label-text);
    font-family: "Open Sans", sans-serif;
    font-weight: 700;
    font-size: 21px;
    letter-spacing: 0.12em;
    display: flex;
    align-items: center;
    justify-content: center;
    white-space: nowrap;
  }
  .tree-illustration {
    position: absolute;
    top: 40px;
    right: 0;
    width: 290px;
    height: 420px;
    background:
      radial-gradient(ellipse at 55% 30%, rgba(233, 201, 46, 0.55), transparent 55%),
      radial-gradient(ellipse at 80% 20%, rgba(124, 191, 58, 0.6), transparent 50%),
      radial-gradient(ellipse at 30% 55%, rgba(154, 111, 182, 0.45), transparent 50%),
      radial-gradient(ellipse at 70% 60%, rgba(63, 159, 214, 0.4), transparent 50%),
      linear-gradient(180deg, rgba(240, 154, 44, 0.25) 0%, rgba(224, 80, 143, 0.2) 55%, rgba(122, 74, 44, 0.55) 100%);
    border-radius: 48% 0 0 30% / 40% 0 0 20%;
  }
  .title-block {
    position: absolute;
    left: 24px;
    right: 24px;
    bottom: 48px;
    color: var(--ink);
    font-family: "Oswald", sans-serif;
  }
  .book-title {
    font-weight: 700;
    font-size: 112px;
    line-height: 0.95;
    letter-spacing: -0.01em;
    text-transform: uppercase;
  }
  .book-title span {
    display: block;
    white-space: nowrap;
  }
  .book-subtitle {
    margin-top: 14px;
    font-weight: 500;
    font-size: 34px;
    line-height: 1.12;
  }
  .book-subtitle span {
    display: block;
    white-space: nowrap;
  }
</style>
</head>
<body>
  <main class="stage">
    <article class="book-cover">
      <div class="tree-illustration" role="img" aria-label="Illustrated tree with a brown trunk and colourful leaves in green, yellow, orange, purple, blue and pink"></div>
      <div class="author-label">NORA PEMBRIDGE</div>
      <div class="title-block">
        <h1 class="book-title"><span>Rooted</span><span>Together</span></h1>
        <p class="book-subtitle"><span>7 Paths to Raise a Household</span><span>that Blooms</span></p>
      </div>
    </article>
  </main>
</body>
</html>
```